依頼詳細
【デザイン改善要望】

・Klipora上のサムネイルのクリック率を上げたいで、インパクトのあるデザインをお願いします。

・Kliporaのサムネイルはやはり人(演者)の写真が入ったほうがインパクトが高いですが、このチャンネルはパペット人形をキャラクターにしているため、人に比べてインパクトが劣ります。そこをデザインの力でインパクトを出したいです。

・キャラクターは「写真」と「イラスト」のどちらも素材として添付しますので、デザインによって、どちらをお使い頂いても構いません。

・サムネイルでチャンネルの世界観を作りたいので、複数枚並んだ時に、全体として統一感が必要です。

【今後の継続依頼】

・今回のコンペで当選した場合、当選者の方にすべてのサムネイルの制作をお願いしたく思っております。

・当選後に別依頼として、50枚25,000円(コモリー受取額・税別)の金額条件にはお受け頂ける方を希望します。

・継続依頼を受けることができない、または、上記の条件では継続依頼を受けることができない方は、コンペへのご応募をお控え頂けますよう、お願い致します。
記載項目
動画キャッチコピー+キャラクター
サイズ
• 「横1280×縦720」×3つ
希望イメージ
シンプル 複雑
単色 カラフル
暗い 明るい
日常 高級
遊び心 厳粛
未来的 伝統的
女性的 男性的
希望する色
納品ファイル
• 高解像度JPG (.jpg)
• イラストレーター形式 (.ai)
• フォトショップ形式 (.psd)
• PNG形式 (.png)
補足説明
■ 選んだ理由

最もイメージに近いデザインをご提案頂き、誠にありがとうございました。また修正にも快く対応頂き、感謝しております。

■ 提案者全員のお礼・コメント

この度は当コンペにご参加頂き、誠にありがとうございました。たくさんの応募を頂き、どれも素晴らしいご提案で、とても選定が難しかったです。またの機会にぜひ宜しくお願い致します。

```html
<!DOCTYPE html>
<html lang="ja">
<head>
<meta charset="utf-8">
<title>サムネイル シリーズ</title>
<link rel="stylesheet" href="https://fonts.googleapis.com/css2?family=M+PLUS+Rounded+1c:wght@800;900&display=swap">
<style>
:root{
  --board:#24452f;
  --board-edge:#1a3323;
  --wood:#8a5a2b;
  --wood-dark:#5e3a17;
  --chalk:#ffffff;
  --accent:#f7a21b;
  --accent-dark:#e0780e;
  --ink:#2b2b2b;
  --yellow:#ffe84a;
  --sky:#cfeefb;
  --pink:#fbd3e4;
  --pink-stripe:#f6bcd5;
  --char-brown:#a87a4d;
  --char-beige:#e8cfa6;
}
*{margin:0;padding:0;box-sizing:border-box}
html,body{width:683px;height:1200px;overflow:hidden;background:#fff}
body{font-family:"M PLUS Rounded 1c",sans-serif;font-weight:900}
.thumb{position:absolute;left:0;width:683px;height:384px;overflow:hidden}
.thumb--one{top:0;background:repeating-linear-gradient(90deg,#d6f0fb 0 18px,#c6e8f7 18px 36px)}
.thumb--two{top:408px;background:repeating-linear-gradient(90deg,var(--pink) 0 18px,var(--pink-stripe) 18px 36px)}
.thumb--three{top:816px;background:linear-gradient(180deg,#fff6b8 0%,#fdf3a8 100%)}
.board{position:absolute;background:var(--board);border:14px solid var(--wood);border-radius:8px;
  box-shadow:inset 0 0 0 3px var(--board-edge),inset 0 0 40px rgba(0,0,0,.35),0 6px 0 var(--wood-dark)}
.board__tray{position:absolute;left:40px;right:40px;bottom:-14px;height:10px;background:var(--wood-dark);border-radius:3px}
.chalk-stick{position:absolute;bottom:-12px;width:34px;height:8px;border-radius:3px}
.label{position:absolute;background:var(--accent);color:var(--ink);padding:4px 18px;border-radius:6px;
  box-shadow:3px 4px 0 rgba(0,0,0,.35);white-space:nowrap}
.line{position:absolute;left:0;right:0;text-align:center;color:var(--chalk);white-space:nowrap;
  text-shadow:0 4px 0 rgba(0,0,0,.35)}
.character{position:absolute;border-radius:48% 48% 40% 40%}
.character--dog{background:linear-gradient(160deg,var(--char-beige),var(--char-brown))}
.character--monkey{background:linear-gradient(160deg,#b8864f,#6b4423)}
.note{color:var(--accent)}
.sky-photo{position:absolute;left:70px;top:150px;width:560px;height:234px;
  background:linear-gradient(180deg,#9fd7f2 0%,#d9f1fb 70%,#b9dff0 100%)}
.banner{position:absolute;left:30px;top:40px;width:623px;height:118px;background:var(--accent-dark);
  border:6px solid #fff;border-radius:14px;box-shadow:0 6px 0 rgba(0,0,0,.2);
  color:#fff;font-size:88px;line-height:104px;text-align:center;letter-spacing:2px;text-shadow:0 4px 0 rgba(0,0,0,.25)}
.subtitle{position:absolute;left:0;right:0;top:176px;text-align:center;font-size:58px;color:var(--accent-dark);
  -webkit-text-stroke:10px #fff;paint-order:stroke fill}
.title-big{position:absolute;left:0;right:0;top:252px;text-align:center;font-size:112px;color:var(--ink);
  -webkit-text-stroke:14px #fff;paint-order:stroke fill;letter-spacing:6px;line-height:1.1}
</style>
</head>
<body>

<section class="thumb thumb--one">
  <div class="board" style="left:58px;top:14px;width:566px;height:348px">
    <div class="label" style="left:14px;top:10px;font-size:40px;transform:rotate(-2deg)">相手を動かす<span style="color:#2e8a3c">♪</span></div>
    <div class="line" style="top:86px;font-size:50px">コミュニケーション</div>
    <div class="line" style="top:160px;font-size:48px">伝え方で</div>
    <div class="line" style="top:226px;font-size:54px">人生は変わる</div>
    <div class="board__tray"></div>
    <span class="chalk-stick" style="left:330px;background:#ff8fb8"></span>
    <span class="chalk-stick" style="left:375px;background:#7fd1f5"></span>
  </div>
  <div class="character character--dog" role="img" aria-label="鹿の角をつけたパペットキャラクターのイラスト" style="left:0;top:250px;width:96px;height:134px"></div>
  <div class="character character--monkey" role="img" aria-label="猿のパペットキャラクターのイラスト" style="left:602px;top:30px;width:81px;height:110px"></div>
</section>

<section class="thumb thumb--two">
  <div class="board" style="left:50px;top:12px;width:566px;height:348px">
    <div class="label" style="left:10px;top:24px;font-size:42px;transform:rotate(-2deg)">仕事がうまくいく</div>
    <div class="line" style="top:112px;font-size:92px;color:var(--yellow)">キャラ<span style="font-size:54px;color:#fff">の</span></div>
    <div class="line" style="top:232px;font-size:58px">作り方</div>
    <div class="board__tray"></div>
    <span class="chalk-stick" style="left:300px;background:#ffffff"></span>
    <span class="chalk-stick" style="left:345px;background:#ff8fb8"></span>
  </div>
  <div class="character character--dog" role="img" aria-label="鹿の角をつけたパペットキャラクターのイラスト" style="left:0;top:60px;width:100px;height:140px"></div>
  <div class="character character--monkey" role="img" aria-label="猿のパペットキャラクターのイラスト" style="left:596px;top:210px;width:87px;height:150px"></div>
</section>

<section class="thumb thumb--three">
  <div class="sky-photo" role="img" aria-label="青空と窓辺の写真"></div>
  <div class="banner">プレゼンで</div>
  <div class="subtitle">使える<span style="font-size:40px">♪</span></div>
  <div class="title-big">言い回し</div>
  <div class="character character--dog" role="img" aria-label="鹿の角をつけたパペットキャラクターのイラスト" style="left:6px;top:250px;width:96px;height:134px"></div>
  <div class="character character--monkey" role="img" aria-label="猿のパペットキャラクターのイラスト" style="left:580px;top:150px;width:100px;height:120px"></div>
</section>

</body>
</html>
```